Website redesign for a national printing company

Our current website is dated and boring: ridgefieldpennants.com

We are looking for a fresh, modern design. We need a clean, minimal design that is also elegant, really shows off large, bright photos of our banners in action and POPS. Our goal is to showcase our beautiful banners, while also giving the user the confidence in our company that we will provide friendly, fast service, fast printing, and deliver their banners on time for their event.

I want a nice flow to the website, the design should tie in well with the printing feel. Here is an example of clean, beautiful design that ties in to the industry - https://www.vorly.com/ - notice how the buttons are like chat icons, for example.

More examples:

Nice clean design https://www.plimbask.com/

https://grevaltic.com/ nice and clean, but it POPS really well.

I like https://www.tarmenvok.com/

https://www.wobrel.com/ gorgeous site, clean, modern

Beautiful, simple, clean, modern - https://fenquatro.com/en-us/

These websites are not from the print industry, that’s because most printers don’t have good websites - they are more focused on local businesses, referrals, not really online marketing.

But keep in mind in your design that we need to give the feel that we are printing their banners beautifully, fast, with great service.

https://www.ambergrale.com/ so clean, bold, clear to the user what the company does. Love this simple yet elegant design.

https://www.q7.com/ - so pretty! And still so simple and obvious to the user what to do on their site.

https://zolvex.com/

https://quarnelby.com/us/en/ big and bold - yet super nicely designed with so many nice touches

https://postwrenly.com/ - also clean, simple, and so obvious to the user to take action and contact the company
Updates

I just updated the job brief, and you can also view it in full here - https://files.vendrolax.com/document/d/7Rmq3ZTp9Lx2Nb8Ck4Hs6Wv0Jd5Fy1Ga3Ue8Oi2Pt/edit?usp=sharing

Target Market(s)

Please read this customer persona - https://files.vendrolax.com/document/d/7Rmq3ZTp9Lx2Nb8Ck4Hs6Wv0Jd5Fy1Ga3Ue8Oi2Pt/edit?usp=sharing

Industry/Entity Type

Printing

Number of Pages Required

1 page

Requirements
Must have
• Nice flow to the website, the design should tie in well with the printing feel. Here is an example of clean, beautiful design that ties in to the industry - https://www.vorly.com/ - notice how the buttons are like chat icons, for example.
Should not have
• No filters on the images, we want large, beautiful images.

```html
<!DOCTYPE html>
<html lang="en">
<head>
<meta charset="utf-8">
<title>Ridgefield Pennants — Printing Plans</title>
<link rel="stylesheet" href="https://fonts.googleapis.com/css2?family=Montserrat:wght@400;500;600;700;800;900&display=swap">
<style>
:root{
  --blue:#1f4fcc;
  --blue-deep:#173fae;
  --navy:#0a1838;
  --navy-2:#0f2452;
  --ink:#111522;
  --text:#4a4f5c;
  --muted:#8b909c;
  --line:#d9dce4;
  --white:#ffffff;
  --gray-band:#c9ccd3;
  --star:#f5b400;
}
*{box-sizing:border-box;margin:0;padding:0}
html,body{width:1200px;height:3776px;overflow:hidden}
body{font-family:"Montserrat",Arial,sans-serif;color:var(--ink);background:var(--white);position:relative}
section,header,footer{position:absolute;left:0;width:1200px}
.abs{position:absolute}
.btn{display:inline-block;font-weight:700;font-size:11px;letter-spacing:.5px;text-transform:uppercase;padding:10px 18px;border-radius:16px 16px 16px 3px}
.btn-blue{background:var(--blue);color:var(--white)}
.btn-white{background:var(--white);color:var(--blue)}
.btn-dark{background:var(--navy);color:var(--white)}
.eyebrow{font-size:12px;font-weight:700;color:var(--blue)}
.h2{font-size:46px;font-weight:900;line-height:1.02;color:var(--ink)}
.para{font-size:14px;line-height:1.55;color:var(--text)}
.photo{position:absolute;border-radius:6px}

/* Hero */
.hero{top:0;height:520px;background:var(--blue)}
.hero-photo{position:absolute;left:600px;top:0;width:600px;height:520px;background:linear-gradient(160deg,#9a9ea6 0%,#4b4f58 45%,#1d2028 100%)}
.nav{position:absolute;top:0;left:0;width:1200px;height:46px;display:flex;align-items:center;padding:0 40px}
.brand{font-size:20px;font-weight:800;color:var(--white);display:flex;align-items:center;gap:8px}
.brand-dot{width:12px;height:12px;background:var(--white)}
.menu{position:absolute;left:404px;display:flex;gap:14px;font-size:10px;font-weight:700;color:var(--white)}
.nav-contact{position:absolute;right:40px;font-size:9px;color:var(--white);line-height:1.5;font-weight:600}
.hero-copy{position:absolute;left:136px;top:158px;color:var(--white)}
.hero-copy .kicker{font-size:15px;font-weight:700}
.hero-copy h1{font-size:68px;font-weight:900;line-height:.98;margin-top:6px}
.hero-copy p{font-size:11px;line-height:1.45;width:380px;margin-top:14px;opacity:.9}
.hero-btns{margin-top:16px;display:flex;gap:10px}
.btn-outline{border:2px solid var(--white);color:var(--white);padding:8px 16px}

/* About */
.about{top:520px;height:460px}
.about-copy{position:absolute;left:136px;top:104px;width:420px}
.about-copy .h2{margin-top:6px}
.about-copy .para{margin-top:14px}
.about-copy .btn{margin-top:20px}
.bubble{position:absolute;background:var(--blue);color:var(--white);font-weight:700;font-size:15px;line-height:1.3;padding:18px 22px;border-radius:22px 22px 22px 4px;box-shadow:0 8px 18px rgba(31,79,204,.25)}

/* Quote */
.quote{top:960px;height:400px}
.quote-bg{position:absolute;inset:0;background:radial-gradient(circle at 15% 70%,#163070 0,transparent 28%),radial-gradient(circle at 85% 30%,#163070 0,transparent 24%),var(--navy)}
.quote-inner{position:absolute;left:0;top:120px;width:1200px;text-align:center;color:var(--white)}
.quote-inner h2{font-size:36px;font-weight:800}
.quote-inner p{font-size:10px;width:620px;margin:12px auto 0;line-height:1.5;opacity:.85}
.quote-form{display:flex;justify-content:center;gap:10px;margin-top:26px}
.field{background:var(--white);color:var(--muted);font-size:10px;text-align:left;padding:10px 12px;border-radius:2px;width:170px}
.quote-send{background:#081026;color:var(--white);font-size:10px;font-weight:700;width:230px;padding:10px;border-radius:2px}

/* Products */
.products{top:1360px;height:420px}
.products-copy{position:absolute;left:136px;top:44px;width:430px}
.products-copy .h2{margin-top:6px}
.products-copy .para{margin-top:14px}
.products-copy .btn{margin-top:20px}

/* Cards */
.cards{top:1780px;height:470px}
.card{position:absolute;top:0;width:290px;height:440px;background:var(--white);box-shadow:0 6px 24px rgba(10,24,56,.12);padding:16px}
.card-photo{height:210px;border-radius:4px}
.card h3{font-size:16px;font-weight:800;margin-top:18px;line-height:1.25}
.card p{font-size:10px;line-height:1.55;color:var(--text);margin-top:10px}
.card .btn{margin-top:14px;font-size:9px;padding:8px 14px}
.card-blue{background:var(--blue);color:var(--white)}
.card-blue p{color:#dfe6fb}

/* Reviews */
.reviews{top:2250px;height:590px}
.reviews-bg{position:absolute;inset:0;background:radial-gradient(circle at 10% 20%,#17306e 0,transparent 22%),radial-gradient(circle at 90% 85%,#17306e 0,transparent 26%),var(--navy)}
.reviews-head{position:absolute;top:68px;width:1200px;text-align:center;color:var(--white)}
.reviews-head h2{font-size:36px;font-weight:800}
.reviews-head p{font-size:10px;margin-top:8px;opacity:.8}
.review{position:absolute;top:200px;width:288px;height:200px;background:var(--white);border-radius:6px;padding:22px}
.review p{font-size:11px;line-height:1.55;color:var(--text)}
.stars{color:var(--star);font-size:12px;margin-top:10px;letter-spacing:1px}
.reviewer{display:flex;align-items:center;gap:10px;margin-top:12px}
.avatar{width:36px;height:36px;border-radius:50%;background:linear-gradient(135deg,#c9b29a,#7a6452)}
.reviewer b{font-size:11px;display:block}
.reviewer span{font-size:9px;color:var(--white);background:var(--blue);padding:1px 6px;border-radius:6px}
.arrow{position:absolute;top:470px;width:36px;height:36px;border-radius:50%;background:var(--white);display:flex;align-items:center;justify-content:center}

/* Contact */
.contact{top:2840px;height:460px}
.info-box{position:absolute;left:152px;width:450px;background:var(--blue);border-radius:10px;color:var(--white)}
.info-box svg{position:absolute}
.info-box .label{position:absolute;font-size:14px;font-weight:800}
.contact-copy{position:absolute;left:604px;top:40px;width:440px}
.contact-copy .h2{font-size:42px;margin-top:4px}
.form-label{font-size:10px;color:var(--text);margin-top:12px}
.input{height:26px;border:1px solid var(--line);border-radius:2px;margin-top:4px}
.textarea{height:60px}
.send{margin-top:10px;background:var(--blue);color:var(--white);text-align:center;font-size:11px;font-weight:700;padding:8px;border-radius:2px}

/* Partners */
.partners{top:3300px;height:150px}
.partner-strip{position:absolute;left:80px;top:16px;width:1040px;height:110px;background:var(--white);box-shadow:0 4px 20px rgba(10,24,56,.08);display:flex;align-items:center;justify-content:space-around;font-size:30px;font-weight:600;color:#6b6f78}

/* Footer */
.footer{top:3450px;height:326px;background:var(--blue);color:var(--white)}
.footer .brand{position:absolute;left:136px;top:40px;font-size:22px}
.footer-about{position:absolute;left:136px;top:80px;width:230px;font-size:10px;line-height:1.6;opacity:.9}
.fcol{position:absolute;top:40px}
.fcol h4{font-size:12px;font-weight:800;margin-bottom:12px}
.fcol li{list-style:none;font-size:10px;line-height:2;display:flex;align-items:center;gap:6px}
.fcol li::before{content:"";width:6px;height:6px;border-radius:50%;background:var(--white)}
.socials{position:absolute;left:548px;top:194px;display:flex;gap:8px}
.socials span{width:26px;height:26px;border-radius:50%;background:var(--navy)}
.copyright{position:absolute;left:0;bottom:18px;width:1200px;text-align:center;font-size:9px;opacity:.85}
</style>
</head>
<body>

<header class="hero">
  <div class="hero-photo" role="img" aria-label="Photo of large printed banners on a city building at night"></div>
  <nav class="nav">
    <div class="brand"><span class="brand-dot"></span>Ridgefield Pennants</div>
    <div class="menu"><span>HOME</span><span>ABOUT</span><span>OUR PRODUCTS</span><span>OUR GALLERIES</span><span>CONTACT</span></div>
    <div class="nav-contact">Toll Free: 800-555-0142<br>info@ridgefieldpennants.com</div>
  </nav>
  <div class="hero-copy">
    <div class="kicker">Ridgefield Pennants</div>
    <h1>Printing<br>Plans</h1>
    <p>Large format banners printed fast and delivered on time, with friendly service from the first proof to the final hang.</p>
    <div class="hero-btns"><span class="btn btn-outline">Explore</span><span class="btn btn-dark">Get a Quote</span></div>
  </div>
</header>

<section class="about">
  <div class="about-copy">
    <div class="eyebrow">Who we are!</div>
    <div class="h2">About Ridgefield<br>Pennants</div>
    <p class="para">For over two decades, Ridgefield Pennants has been the go to source for high quality custom printing for large format banners, plastic roll banners, stage backdrops and mobile stage festival banners.</p>
    <span class="btn btn-blue">Learn More</span>
  </div>
  <div class="bubble" style="left:620px;top:100px;width:240px">Customer Service is Always First</div>
  <div class="bubble" style="left:880px;top:80px;width:240px">Customer Service is Always First</div>
  <div class="bubble" style="left:620px;top:224px;width:240px">Making Brands Look Good On Stage For Over Two Decades</div>
  <div class="bubble" style="left:880px;top:276px;width:240px">Quality You Can Count On</div>
</section>

<section class="quote">
  <div class="quote-bg"></div>
  <svg class="abs" style="left:0;top:0" width="1200" height="100" viewBox="0 0 1200 100"><polygon points="0,0 1200,0 1200,20 0,100" fill="#ffffff"/><polygon points="0,40 1200,0 1200,60 0,100" fill="var(--gray-band)" opacity=".7"/></svg>
  <div class="quote-inner">
    <h2>Need a Price Quote? Get in Touch!</h2>
    <p>Tell us about your event, banner sizes and deadline and our team will send back a clear price quote within one business day. Fast turnaround and on time delivery come standard with every order we print.</p>
    <div class="quote-form"><div class="field">Name</div><div class="field">Email</div><div class="field">Phone</div><div class="quote-send">Send</div></div>
  </div>
</section>

<section class="products">
  <div class="products-copy">
    <div class="eyebrow">What we will provide?</div>
    <div class="h2">Our Products</div>
    <p class="para">Lorem ipsum dolor sit amet, consectetur adipiscing elit. Ut elit tellus, luctus nec ullamcorper mattis, pulvinar dapibus leo. Aliquam accommodare duo cu, lus labore iudicabit efficiendi ex, ne vim anim eu, his rebum iriure aliquet graecis ei. Aliquam accommodare duo cu.</p>
    <span class="btn btn-blue">Learn More</span>
  </div>
  <div class="photo" style="left:612px;top:-6px;width:240px;height:160px;background:linear-gradient(150deg,#c3c8d1,#6d7482)" role="img" aria-label="Photo of printed vinyl banners at an outdoor venue"></div>
  <div class="photo" style="left:872px;top:18px;width:200px;height:130px;background:linear-gradient(150deg,#3f63c9,#0d1a45)" role="img" aria-label="Photo of a lit concert stage with a printed backdrop"></div>
  <div class="photo" style="left:660px;top:172px;width:240px;height:150px;background:linear-gradient(160deg,#8fb0d8,#2f3f66)" role="img" aria-label="Photo of a mobile stage wrapped in festival banners"></div>
</section>

<section class="cards">
  <div class="card" style="left:152px">
    <div class="card-photo" style="background:linear-gradient(150deg,#dcdde2,#8c919c)" role="img" aria-label="Photo of plastic roll banners displayed outdoors"></div>
    <h3>Plastic Roll Banners</h3>
    <p>Durable plastic roll banners made for quick setup and easy reuse. Cut to any length you need, printed in bright colour that holds up in sun, wind and rain at events big and small across the season.</p>
    <span class="btn btn-blue">Learn More</span>
  </div>
  <div class="card card-blue" style="left:455px">
    <div class="card-photo" style="background:linear-gradient(150deg,#6b5a7c,#1a1530)" role="img" aria-label="Photo of a festival stage with printed backdrops"></div>
    <h3>Festival Banners and Stage Backdrops</h3>
    <p>Full stage backdrops and festival banners printed at massive sizes, with clean seams and strong grommets, ready to hang on arrival so your crew can set the stage without delay.</p>
    <span class="btn btn-white">Learn More</span>
  </div>
  <div class="card" style="left:758px">
    <div class="card-photo" style="background:linear-gradient(160deg,#a9c3e2,#4d5d74)" role="img" aria-label="Photo of a large format mesh banner on a building"></div>
    <h3>Large Format and Mesh Banners</h3>
    <p>Large format and mesh banners for buildings, fences and arenas. Wind friendly mesh keeps your message standing tall while sharp printing keeps it readable from far across the grounds.</p>
    <span class="btn btn-blue">Learn More</span>
  </div>
</section>

<section class="reviews">
  <div class="reviews-bg"></div>
  <div class="reviews-head">
    <h2>Rated 5/5 Stars By Our Customers</h2>
    <p>Read our reviews from event planners, venues, brands and performers who trust Ridgefield Pennants.</p>
  </div>
  <div class="review" style="left:152px">
    <p>Ridgefield was great to work with. We used them to make banners for our stadium.</p>
    <div class="stars">★★★★★</div>
    <div class="reviewer"><div class="avatar" role="img" aria-label="Customer portrait"></div><div><b>Marla V.</b><span>Verified</span></div></div>
  </div>
  <div class="review" style="left:456px">
    <p>The banner turned out great and was delivered promptly. Looks great on stage.</p>
    <div class="stars">★★★★★</div>
    <div class="reviewer"><div class="avatar" role="img" aria-label="Customer portrait"></div><div><b>Dana Pellow</b><span>Verified</span></div></div>
  </div>
  <div class="review" style="left:760px">
    <p>Rob and the team at Ridgefield have been great to work with. They go to...</p>
    <div class="stars">★★★★★</div>
    <div class="reviewer"><div class="avatar" role="img" aria-label="Customer portrait"></div><div><b>Marla V.</b><span>Verified</span></div></div>
  </div>
  <span class="btn btn-blue abs" style="left:152px;top:478px">Learn More</span>
  <div class="arrow" style="left:960px"><svg width="14" height="14" viewBox="0 0 14 14"><path d="M9 2 4 7l5 5" stroke="#0a1838" stroke-width="2.2" fill="none"/></svg></div>
  <div class="arrow" style="left:1006px"><svg width="14" height="14" viewBox="0 0 14 14"><path d="m5 2 5 5-5 5" stroke="#0a1838" stroke-width="2.2" fill="none"/></svg></div>
</section>

<section class="contact">
  <div class="info-box" style="top:104px;height:150px">
    <svg style="left:150px;top:26px" width="90" height="66" viewBox="0 0 90 66"><rect x="2" y="2" width="86" height="62" rx="6" fill="#fff"/><path d="M4 6 45 38 86 6" stroke="var(--blue)" stroke-width="4" fill="none"/></svg>
    <div class="label" style="left:0;width:450px;text-align:center;top:112px">info@ridgefieldpennants.com</div>
  </div>
  <div class="info-box" style="top:276px;height:160px">
    <svg style="left:186px;top:22px" width="80" height="80" viewBox="0 0 80 80"><circle cx="40" cy="40" r="38" fill="#fff"/><path d="M28 22c3-2 6 0 7 3l2 6c1 2 0 4-2 5l-3 2c2 5 6 9 11 11l2-3c1-2 3-3 5-2l6 2c3 1 5 4 3 7-3 5-9 7-15 4-10-5-17-12-21-22-2-6 0-11 5-13z" fill="var(--blue)"/></svg>
    <div class="label" style="left:0;width:450px;text-align:center;top:122px">800-555-0142 / 724-555-0198</div>
  </div>
  <div class="contact-copy">
    <div class="eyebrow" style="color:var(--ink)">Contact us</div>
    <div class="h2">Need a help?<br>Don't worry just<br>contact us</div>
    <div class="form-label">Name</div><div class="input"></div>
    <div class="form-label">Email</div><div class="input"></div>
    <div class="form-label">Message</div><div class="input textarea"></div>
    <div class="send">Send</div>
  </div>
</section>

<section class="partners">
  <div class="partner-strip"><span>Harbin Media Group</span><span>Brookline Radio</span><span>Localoop</span><span>Corey Hale</span></div>
</section>

<footer class="footer">
  <div class="brand"><span class="brand-dot"></span>Ridgefield Pennants</div>
  <p class="footer-about">For over two decades, Ridgefield Pennants has been the go to source for high quality custom printing for large format banners, plastic roll banners, stage backdrops and mobile stage festival banners.</p>
  <div class="fcol" style="left:430px"><h4>Quick Links</h4><ul><li>Home</li><li>About</li><li>Our Products</li><li>Gallery</li><li>Contact</li></ul></div>
  <div class="fcol" style="left:548px"><h4>Our Products</h4><ul><li>Plastic Roll Banners</li><li>Festival Banners and Stage Backdrops</li><li>Large Format and Mesh Banners</li></ul></div>
  <div class="socials"><span></span><span></span><span></span></div>
  <div class="fcol" style="left:830px"><h4>Extras</h4><ul><li>Request a Catalog</li><li>Print Guide</li><li>Artwork</li><li>FAQ</li><li>Customer Reviews</li></ul></div>
  <div class="fcol" style="left:960px;top:66px"><ul><li>Customer Sales Contract</li><li>Privacy Policy</li></ul></div>
  <div class="copyright">Copyright © 2024 Ridgefield Pennants. All rights reserved.</div>
</footer>

</body>
</html>
```